Helicopter company requires newspaper ad

"Ridgeline Aviation" is an agricultural helicopter company based in Victoria, Australia. We need an advert design for use in newspapers and also possibly social media. Our company specialises in using a helicopter for various agricultural work such as Spraying weeds ("Cropdusting"), spreading fertiliser. This advert will be targeted at farmers in our service area, Our customers are mainly dairy and cow farmers and our services are aimed at increasing their farm productivity. The final design should inform potential and existing customers about our services and the benefits of them. I will attach files of our logo and some existing advertising material for guidance. We would like the ad to feature the blue and green colours in our logo Please feel free to view our website and facebook page to see more about what we do. www.ridgelineaviation.com.au Some text we would like included Spraying: -Accurate -Time Efficient -Zero crop damage -Cost efficient Fertiliser Spreading: -Accurate, Pattern-tested equipment -Zero crop damage or wheel marks -Ability to load product out of a truck, bin or bulk bags -Cost effective, Prices from $32 per hectare depending on spread rate The final advert size should be 195 mm wide x 186 mm high Thanks :)

Farmers, Agriculture Industry

Agribusiness

Designer to choose colors to be used in the design.

• Phone number 0491 736 058
• The text included in the decription, or variations of this

```html
<!DOCTYPE html>
<html lang="en">
<head>
<meta charset="utf-8">
<title>Ridgeline Aviation – Aerial Spraying &amp; Spreading</title>
<link rel="stylesheet" href="https://fonts.googleapis.com/css2?family=Old+Standard+TT:wght@400;700&family=Tinos:wght@700&display=swap">
<style>
  :root {
    --ink: #111410;
    --leaf-light: #c9e59a;
    --leaf: #8fb34e;
    --leaf-deep: #2f5a16;
    --field-dark: #172c0b;
    --heading-green: #9ccb5b;
    --frame: #9fb98a;
    --sky-top: #3f7fd6;
    --sky-low: #8fbde6;
    --brand-blue: #1b4f96;
    --paper: #ffffff;
    --text-green: #2a3d12;
  }
  * { margin: 0; padding: 0; box-sizing: border-box; }
  html, body { width: 1200px; height: 1144px; overflow: hidden; background: var(--paper); }
  .ad { position: relative; width: 1200px; height: 1144px; overflow: hidden; font-family: "Old Standard TT", serif; }
  .ad-art { position: absolute; inset: 0; width: 1200px; height: 1144px; }
  .headline { position: absolute; color: var(--ink); font-weight: 700; line-height: 1; white-space: nowrap; }
  .headline--lead { left: 70px; top: 54px; font-size: 37px; letter-spacing: 0.5px; }
  .headline--main { left: 66px; top: 96px; font-size: 50px; }
  .headline--main small { font-size: 32px; }
  .headline--end { left: 316px; top: 162px; font-size: 46px; letter-spacing: 1px; }
  .brand { position: absolute; left: 905px; top: 110px; display: flex; align-items: center; gap: 10px;
           color: var(--brand-blue); font-weight: 700; font-size: 27px; line-height: 1.05; }
  .brand-dot { width: 22px; height: 22px; border-radius: 50%; background: var(--leaf); flex: none; }
  .service-title { position: absolute; color: var(--heading-green); font-weight: 700; font-size: 27px; letter-spacing: 1px; }
  .service-title--spray { left: 320px; top: 814px; }
  .service-title--spread { left: 715px; top: 805px; }
  .spray-list { position: absolute; left: 400px; top: 852px; list-style: none; color: var(--paper);
                font-weight: 700; font-size: 22px; line-height: 32px; letter-spacing: 0.8px; }
  .spray-list li::before { content: "•"; margin-right: 4px; color: #dfe8d6; }
  .spread-list { position: absolute; left: 780px; top: 843px; width: 360px; list-style: none; color: var(--paper);
                 font-family: "Tinos", serif; font-weight: 700; font-size: 17px; line-height: 22px; letter-spacing: -0.4px; }
  .spread-list li { margin-bottom: 7px; }
  .contact-bar { position: absolute; left: 118px; top: 1021px; width: 953px; height: 102px; background: var(--paper);
                 display: flex; align-items: center; }
  .contact-owner { width: 371px; padding-left: 21px; color: var(--text-green); font-weight: 700; font-size: 20px; letter-spacing: 1px; }
  .contact-rule { width: 5px; height: 92px; background: var(--leaf-deep); }
  .contact-details { flex: 1; text-align: center; line-height: 1; }
  .contact-tagline { color: var(--text-green); font-weight: 700; font-size: 26px; letter-spacing: 1px; }
  .contact-phone { color: var(--brand-blue); font-weight: 700; font-size: 30px; margin-top: 6px; letter-spacing: 1px; }
  .contact-web { color: var(--text-green); font-weight: 700; font-size: 21px; margin-top: 4px; letter-spacing: 1.2px; }
</style>
</head>
<body>
<main class="ad">
  <svg class="ad-art" viewBox="117 111 1303 1241" preserveAspectRatio="none" aria-hidden="false">
    <defs>
      <linearGradient id="top-wash" x1="0" y1="0" x2="1" y2="0.4">
        <stop offset="0" stop-color="#6f9a3c"/>
        <stop offset="0.35" stop-color="#b6d98a"/>
        <stop offset="0.75" stop-color="#eef5e2"/>
        <stop offset="1" stop-color="#ffffff"/>
      </linearGradient>
      <linearGradient id="field" x1="0" y1="0" x2="0" y2="1">
        <stop offset="0" stop-color="#4d7a24"/>
        <stop offset="0.5" stop-color="#2c5213"/>
        <stop offset="1" stop-color="#132508"/>
      </linearGradient>
      <linearGradient id="sky" x1="0" y1="0" x2="0" y2="1">
        <stop offset="0" stop-color="#3c7bd4"/>
        <stop offset="0.75" stop-color="#8cbbe6"/>
        <stop offset="0.88" stop-color="#6f9a52"/>
        <stop offset="1" stop-color="#4e7d2e"/>
      </linearGradient>
      <linearGradient id="spray-scene" x1="0" y1="0" x2="0" y2="1">
        <stop offset="0" stop-color="#a9cbe6"/>
        <stop offset="0.6" stop-color="#dfe8ee"/>
        <stop offset="0.85" stop-color="#c7d2c4"/>
        <stop offset="1" stop-color="#5f8f32"/>
      </linearGradient>
    </defs>
    <rect x="117" y="111" width="1303" height="1241" fill="url(#top-wash)"/>
    <path d="M117 420 Q500 330 1000 470 L1420 470 L1420 1352 L117 1352 Z" fill="url(#field)"
          role="img" aria-label="Rolling green pasture fields"/>
    <polygon points="565,465 1420,465 1420,975 605,975 540,700" fill="none" stroke="var(--frame)" stroke-width="10" opacity="0.8"/>
    <polygon points="570,478 1420,478 1420,963 612,963 548,700" fill="url(#sky)"
             role="img" aria-label="Helicopter spreading fertiliser from an underslung bucket over green hills"/>
    <g role="img" aria-label="Helicopter spraying a crop with boom spray, shown across diamond panels" stroke="var(--frame)" stroke-width="8" fill="url(#spray-scene)">
      <polygon points="336,318 525,505 336,692 149,505"/>
      <polygon points="145,520 335,710 145,900 -45,710"/>
      <polygon points="540,520 730,705 540,890 350,705"/>
      <polygon points="340,712 530,900 340,1092 152,900"/>
    </g>
  </svg>

  <h1 class="headline headline--lead">SUMMER CROPS NEED</h1>
  <p class="headline headline--main">SPRAYING <small>(or)</small></p>
  <p class="headline headline--end">FERTILISER?</p>

  <div class="brand"><span class="brand-dot"></span><span>Ridgeline<br>Aviation</span></div>

  <h2 class="service-title service-title--spray">SPRAYING:</h2>
  <ul class="spray-list">
    <li>ACCURATE</li>
    <li>TIME EFFICIENT</li>
    <li>ZERO CROP DAMAGE</li>
    <li>COST EFFECTIVE</li>
  </ul>

  <h2 class="service-title service-title--spread">SPREADING:</h2>
  <ul class="spread-list">
    <li>Accurate, pattern-tested equipment</li>
    <li>Zero crop damage or wheel marks</li>
    <li>Ability to load out of a Truck, Bin or Bulk-bags</li>
    <li>Competitive prices(from $32 per hectare depending on spread rate)</li>
  </ul>

  <footer class="contact-bar">
    <p class="contact-owner">OWNER/OPERATED</p>
    <span class="contact-rule"></span>
    <div class="contact-details">
      <p class="contact-tagline">Aerial Agriculture Specialist</p>
      <p class="contact-phone">0491 736 058</p>
      <p class="contact-web">www.ridgelineaviation.com.au</p>
    </div>
  </footer>
</main>
</body>
</html>
```